Wedding Invitations

We are a printing company "inkmakers" and require multiple wedding invitation designs for our customers in store and online. We would like the designs to be editable in Photoshop if possible, if not then a layout with suggested fonts would be the next best option. We are open to suggestions on design but would like to stick to the general wedding themes some with a modern and some with a classical feel

Industry/Entity Type

Printing

```html
<!DOCTYPE html>
<html lang="en">
<head>
<meta charset="utf-8">
<title>Wedding Invitation</title>
<link rel="stylesheet" href="https://fonts.googleapis.com/css2?family=Great+Vibes&family=Tinos&display=swap">
<style>
  :root {
    --plum: #7d2e93;
    --plum-deep: #4e1d57;
    --marigold: #f9d56c;
    --sunset: #d9492a;
    --ivory: #ffffff;
  }
  * { margin: 0; padding: 0; box-sizing: border-box; }
  html, body { width: 1200px; height: 848px; overflow: hidden; background: var(--plum); }
  .invitation {
    position: relative;
    width: 1200px;
    height: 848px;
    background: var(--plum);
    font-family: "Tinos", "Times New Roman", serif;
    color: var(--ivory);
    overflow: hidden;
  }
  .line { position: absolute; white-space: nowrap; line-height: 1; }
  .families { left: 349px; top: 58px; font-size: 20px; transform: translateX(-50%); }
  .script {
    font-family: "Great Vibes", cursive;
    color: var(--marigold);
    font-size: 64px;
  }
  .bride { left: 122px; top: 108px; }
  .ampersand { left: 288px; top: 180px; font-size: 42px; }
  .groom { left: 280px; top: 248px; }

  .details { position: absolute; left: 857px; transform: translateX(-50%); text-align: center; }
  .details p { position: absolute; left: 0; transform: translateX(-50%); white-space: nowrap; line-height: 1; }
  .invite { font-size: 22px; }
  .when { font-size: 21px; }
  .where { font-size: 21px; }

  .rsvp {
    position: absolute;
    right: 39px;
    top: 732px;
    text-align: right;
    font-size: 17px;
    line-height: 22px;
  }

  .lovebirds {
    position: absolute;
    left: 676px;
    top: 40px;
    width: 366px;
    height: 294px;
    border-radius: 46% 46% 40% 40%;
    background: radial-gradient(ellipse at 35% 70%, var(--sunset) 0%, rgba(217,73,42,0.55) 35%, transparent 60%),
                radial-gradient(ellipse at 70% 70%, var(--marigold) 0%, rgba(249,213,108,0.55) 35%, transparent 60%),
                radial-gradient(ellipse at 55% 18%, var(--plum-deep) 0%, rgba(78,29,87,0.6) 25%, transparent 45%);
  }
  .floral { position: absolute; left: 0; top: 290px; width: 670px; height: 558px; }
</style>
</head>
<body>
<main class="invitation">
  <p class="line families">TOGETHER WITH THEIR FAMILIES</p>
  <p class="line script bride">Bride</p>
  <p class="line ampersand">&amp;</p>
  <p class="line script groom">Bride groom</p>

  <div class="lovebirds" role="img" aria-label="Illustration of two kissing birds, one orange and one yellow, beneath hearts"></div>

  <svg class="floral" viewBox="0 0 670 558" role="img" aria-label="Decorative floral bouquet of purple, orange and yellow flowers, leaves and swirls">
    <defs>
      <radialGradient id="bloom" cx="0.2" cy="0.85" r="0.9">
        <stop offset="0" stop-color="#4e1d57"/>
        <stop offset="0.45" stop-color="#d9492a" stop-opacity="0.75"/>
        <stop offset="0.8" stop-color="#f9d56c" stop-opacity="0.45"/>
        <stop offset="1" stop-color="#f9d56c" stop-opacity="0"/>
      </radialGradient>
    </defs>
    <path d="M0 70 C40 20 110 0 160 60 C210 120 250 240 320 300 C400 360 520 380 600 430 C650 465 670 520 665 558 L0 558 Z" fill="url(#bloom)"/>
  </svg>

  <section class="details" style="top:0;">
    <p class="invite" style="top:368px;">INVITE YOU TO SHARE IN THEIR</p>
    <p class="invite" style="top:410px;">WEDDING CELEBRATION</p>
    <p class="when" style="top:483px;">SATURDAY, THE TWENTY-SECOND OF DECEMBER</p>
    <p class="when" style="top:522px;">TWO THOUSAND AND FOURTEEN</p>
    <p class="when" style="top:566px;">TWO O’CLOCK THE AFTERNOON</p>
    <p class="where" style="top:638px;">ANYWHERE HOTEL</p>
    <p class="where" style="top:671px;">CITY, STATE</p>
  </section>

  <div class="rsvp">
    <p>RSVP</p>
    <p>by date</p>
    <p>phone number</p>
  </div>
</main>
</body>
</html>
```